I need a business card design for my new chiropractic business.It is chiropractic that addresses the whole body, is natural, done by hand, will reduce pain, increase vitality, reduce stress. It is safe and suitable for all ages.I am a Ravenhale chiropractor and they have a particular logo see RCA.co.uk. I would like Spineleaf Chiropractic and Ravenhale to feature if possible. Purple colours and tones please.

Target Market(s)

People who are interested in their health and being empowered to take responsibility for their well being.

Industry/Entity Type

Business

Contact Information for Business Card

My name, Marla Denton
PSB Reg No 05192
Tel No 07914 118275

Font styles to use
Sans Serif
Other font styles liked:
• ITALIC?

Colors
b768aa
886aae
a6459a
6c459b
ffffff
e567a6

Requirements
Must have
• graphic to represent healing by hand and increase in well being. by restoring spinal and nervous system function.
• Professional and clear layout and information
• Some or all of the words above in project description
• Ravenhale logo (from ravenhalechiropractic.org).
Nice to have
• Transformative theme- body- from pain to freedom of motion. A more fully integrated
• System, better functioning and connections.
• Clear layout and message
Should not have
• Must not look tacky

```html
<!DOCTYPE html>
<html lang="en">
<head>
<meta charset="utf-8">
<title>Ravenhale Chiropractic – Business Card</title>
<link href="https://fonts.googleapis.com/css2?family=Arimo:ital,wght@0,400;0,700;1,400&display=swap" rel="stylesheet">
<style>
  :root {
    --page-bg: #e9e6ec;
    --foliage-deep: #2a1530;
    --foliage-mid: #5a3468;
    --foliage-light: #8a5d96;
    --hands-skin: #d9a58f;
    --hands-glow: #ffc36a;
    --panel: rgba(255, 255, 255, 0.16);
    --panel-dark: rgba(40, 40, 48, 0.55);
    --band: #4a2552;
    --band-edge: #6c459b;
    --text-light: #ffffff;
    --text-soft: #ece6f0;
  }
  * { box-sizing: border-box; margin: 0; padding: 0; }
  html, body {
    width: 1200px;
    height: 800px;
    overflow: hidden;
    background: var(--page-bg);
    font-family: "Arimo", Arial, sans-serif;
  }
  .business-card {
    position: absolute;
    left: 100px;
    top: 110px;
    width: 1000px;
    height: 580px;
    overflow: hidden;
    border-radius: 4px;
    box-shadow: 0 10px 30px rgba(40, 20, 50, 0.25);
  }
  .foliage-photo {
    position: absolute;
    inset: 0;
    background:
      radial-gradient(ellipse at 30% 70%, var(--foliage-light) 0%, transparent 45%),
      radial-gradient(ellipse at 85% 30%, var(--foliage-mid) 0%, transparent 50%),
      linear-gradient(160deg, var(--foliage-deep) 0%, var(--foliage-mid) 55%, var(--foliage-deep) 100%);
  }
  .hands-photo {
    position: absolute;
    left: 430px;
    top: 0;
    width: 390px;
    height: 420px;
    border-radius: 0 0 45% 45%;
    background:
      radial-gradient(circle at 45% 48%, var(--hands-glow) 0%, rgba(255, 160, 90, 0.6) 14%, transparent 34%),
      radial-gradient(ellipse at 50% 50%, var(--hands-skin) 0%, rgba(200, 150, 150, 0.7) 45%, transparent 72%);
  }
  .logo-panel {
    position: absolute;
    left: 0;
    top: 95px;
    width: 400px;
    height: 165px;
    background: var(--panel);
    padding: 40px 0 0 50px;
  }
  .logo-lockup {
    display: flex;
    align-items: center;
    gap: 14px;
  }
  .logo-mark {
    width: 54px;
    height: 54px;
    border-radius: 50%;
    background: var(--text-light);
  }
  .logo-name {
    color: var(--text-light);
    font-weight: 400;
    font-size: 24px;
    letter-spacing: 0.5px;
    line-height: 1.15;
  }
  .tagline {
    margin-top: 18px;
    color: var(--text-soft);
    font-style: italic;
    font-size: 17px;
    letter-spacing: 0.5px;
  }
  .holder {
    position: absolute;
    left: 62px;
    top: 300px;
    color: var(--text-light);
  }
  .holder-name {
    font-weight: 700;
    font-size: 38px;
    letter-spacing: -1px;
  }
  .holder-role {
    margin: 2px 0 0 150px;
    font-weight: 700;
    font-size: 18px;
  }
  .contact-panel {
    position: absolute;
    right: 0;
    top: 370px;
    width: 300px;
    height: 115px;
    background: var(--panel-dark);
    padding: 34px 0 0 24px;
    color: var(--text-light);
    font-weight: 700;
    font-size: 17px;
    line-height: 1.35;
  }
  .contact-row {
    display: grid;
    grid-template-columns: 112px auto;
    white-space: nowrap;
  }
  .bottom-band {
    position: absolute;
    left: 0;
    right: 0;
    bottom: 0;
    height: 30px;
    background: linear-gradient(var(--band-edge), var(--band));
  }
</style>
</head>
<body>
  <article class="business-card">
    <div class="foliage-photo" role="img" aria-label="Purple-toned foliage photograph filling the card background"></div>
    <div class="hands-photo" role="img" aria-label="Photograph of two cupped open hands holding a warm glowing light"></div>

    <div class="logo-panel">
      <div class="logo-lockup">
        <span class="logo-mark"></span>
        <span class="logo-name">Ravenhale Chiropractic</span>
      </div>
      <p class="tagline">...supporting your natural balance...</p>
    </div>

    <div class="holder">
      <p class="holder-name">Marla Denton</p>
      <p class="holder-role">Manager</p>
    </div>

    <div class="contact-panel">
      <p class="contact-row"><span>PSB Reg No</span><span>: 05192</span></p>
      <p class="contact-row"><span>Tel No</span><span>: 07914 118275</span></p>
    </div>

    <div class="bottom-band"></div>
  </article>
</body>
</html>
```